Clean, Throwback Album Art needed

I'm looking for album art for an Indie Rock EP titled "The Quiet Lantern". The artist name is "Martin Kowalczyk"

I'm looking for a design that's wistful and nostalgic, but not depressing. I'm more interested in creative patterns and color combinations than anything else. I've uploaded two examples of album art I really like.

Please no stock images.

In addition to the album art, I will also need two variants of a back cover created in a complementary style- one with a track listing and one with marketing copy (e.g. Free download available at ___ ). These back covers do not have to be incredibly detailed, but can't just be text overlaid on top of of the front cover.

Details for back cover (track names, credits, etc.) will be provided to whoever submits the winning front cover design.

Requirements
Should not have
• No stock images. I need to know that I fully own the copyright to whatever work is produced.

```html
<!DOCTYPE html>
<html lang="en">
<head>
<meta charset="utf-8">
<title>Martin Kowalczyk – The Quiet Lantern</title>
<link rel="stylesheet" href="https://fonts.googleapis.com/css2?family=Staatliches&family=Josefin+Sans:wght@300&display=swap">
<style>
  :root {
    --fire-deep: #7a2a12;
    --fire-mid: #e0761f;
    --fire-glow: #f8c25a;
    --haze: #f6efe6;
    --ice-dark: #2c4a60;
    --ice-mid: #8fb0c4;
    --ice-light: #d7e4ea;
    --frame: #ffffff;
    --title: #ffffff;
    --subtitle-dark: #2a2a2a;
    --subtitle-light: #f4f8fa;
  }
  html, body {
    margin: 0;
    padding: 0;
    width: 1200px;
    height: 1199px;
    overflow: hidden;
    background: #ffffff;
  }
  .cover {
    position: relative;
    width: 1200px;
    height: 1199px;
    overflow: hidden;
  }
  .artwork-fire {
    position: absolute;
    left: 0; top: 0;
    width: 618px; height: 1199px;
    background:
      radial-gradient(ellipse 420px 520px at 300px 470px, var(--fire-glow) 0%, var(--fire-mid) 45%, rgba(224,118,31,0) 75%),
      radial-gradient(ellipse 500px 300px at 250px 60px, var(--fire-deep) 0%, rgba(122,42,18,0) 80%),
      linear-gradient(180deg, #c8672a 0%, #e9b27a 40%, var(--haze) 75%, #ece8e4 100%);
  }
  .artwork-ice {
    position: absolute;
    left: 618px; top: 0;
    width: 582px; height: 1199px;
    background:
      radial-gradient(ellipse 260px 420px at 560px 820px, var(--ice-dark) 0%, rgba(44,74,96,0) 80%),
      radial-gradient(ellipse 300px 200px at 480px 40px, #4a6a80 0%, rgba(74,106,128,0) 80%),
      linear-gradient(180deg, #9fb9c8 0%, var(--ice-light) 45%, var(--ice-mid) 80%, #7f9fb3 100%);
  }
  .frame {
    position: absolute;
    left: 36px; top: 36px;
    width: 1128px; height: 1128px;
    box-sizing: border-box;
    border: 2px solid var(--frame);
  }
  .artist-name {
    position: absolute;
    left: 0; top: 68px;
    width: 1200px;
    margin: 0;
    text-align: center;
    font-family: "Staatliches", "Impact", sans-serif;
    font-weight: 400;
    font-size: 148px;
    line-height: 1;
    letter-spacing: 4px;
    color: var(--title);
  }
  .release-title {
    position: absolute;
    left: 0; top: 1136px;
    width: 1200px;
    margin: 0;
    text-align: center;
    font-family: "Josefin Sans", "Helvetica Neue", sans-serif;
    font-weight: 300;
    font-size: 30px;
    line-height: 1;
    letter-spacing: 30px;
    text-indent: 30px;
  }
  .release-title .on-fire { color: var(--subtitle-dark); }
  .release-title .on-ice { color: var(--subtitle-light); }
</style>
</head>
<body>
  <main class="cover">
    <div class="artwork-fire" role="img" aria-label="Left half of a bare tree engulfed in orange flames against a pale hazy sky"></div>
    <div class="artwork-ice" role="img" aria-label="Right half of the same bare tree in a cold blue winter storm with blowing snow"></div>
    <div class="frame"></div>
    <h1 class="artist-name">Martin Kowalczyk</h1>
    <p class="release-title"><span class="on-fire">THE QUIET </span><span class="on-ice">LANTERN</span></p>
  </main>
</body>
</html>
```